TKR Website Overhaul. Complete new website look and function.

Need our website overhauled to be updated so it aligns better with our current cliental. We have competitors to compare to. The purpose of the site has changed and is no longer sales based. This site needs to qualify us and allow consultants and engineers to just discover our background and differentiators. I have attached a company profile from a recent project to provide a better idea. This profile is directed towards the specific project however so that would need to be edited out. Competitor websites that we would want to be comparable to would include: https://www.velmorbuild.com/ , https://tamblinconstruction.ca/ , https://www.pikeconstruction.ca/ , https://steadfastdiggers.com/ , https://www.lunacrestconstruction.ca/. These are all competitors so nothing can be directly copied. I have attached our logo's however I don't think they need to be directly used on the site or maybe they need to be changed to not include color etc. We need to have a more professional look and these colorful logos are hard to pull that off with other than maybe the all gold TKR prime contracting logo with a rich dark green background or something. Green has been our main color over the years and the leaf follows us as the core item in logos. Go with a gold leaf look or something. Our main focus is General Contracting (Prime Contracting) and civil construction. We are a home builder however we would do a second website for that so we don't want to include it. I don't mind a ton of generic civil and general contractor information etc on the site. I don't really need a portfolio of pictures showing on the site but job history etc is very common in the industry and that information can be found in the company profile attached. First Nation work is a big part of our portfolio but we have worked in mining, industrial, oil and gas as well. Municipal sewer and water is our main focus for civil construction though and is a big part of our First Nation work as well.

Industry/Entity Type

General Contractor and Civil Construction

Coding

Coded - Design and coding required

Number of Pages Required

5+ page

Font styles to use
Other font styles liked:
• A mix of Times New Roman, script and serif to create a very professional with a touch of elegance to match our leafed prime contractor logo.

Colors
00AB8E
00BBA5
67D7C9
C6EFE9
E9F9F6

Requirements
Must have
• A rich high end professional look. This company completes government work and is often looked at by executives. A menu that includes About, Our Work, Methodology, Join Our Team and Contact
Nice to have
• Some generic general pictures of municipal underground water work and general contractor building work. I am looking for a rich green darker greens where it matters but with more real world feel overall. So images and movement is good. Civil underground water and sewer, storm water, retention ponds, and process plant and electrical (such as water treatment plants), background imagery is good to have. I like to have things faded out in the background more than in your face.
Should not have
• brighter colors.

```html
<!DOCTYPE html>
<html lang="en">
<head>
<meta charset="utf-8">
<title>TKR Prime Contracting — Commercial and Civil Construction</title>
<link rel="stylesheet" href="https://fonts.googleapis.com/css2?family=Cinzel:wght@500;600;700&family=Lato:wght@400;700&display=swap">
<style>
:root{
  --forest:#0c3a2b;
  --forest-deep:#082b20;
  --teal:#17967a;
  --teal-bright:#00ab8e;
  --mint:#c6efe9;
  --mint-pale:#e9f9f6;
  --gold:#b98a2e;
  --gold-light:#d8b15a;
  --ink:#1d2a26;
  --muted:#4c5b56;
  --white:#ffffff;
  --serif:'Cinzel', 'Times New Roman', serif;
  --sans:'Lato', Arial, sans-serif;
}
*{box-sizing:border-box;margin:0;padding:0}
html,body{width:1200px;height:4192px;overflow:hidden}
body{font-family:var(--sans);color:var(--ink);background:var(--white);position:relative}
.btn{display:inline-block;background:var(--gold);color:var(--white);font:700 13px/1 var(--sans);letter-spacing:.08em;text-transform:uppercase;padding:13px 22px;border-radius:3px;text-decoration:none}
.section-title{font-family:var(--serif);font-weight:600;color:var(--forest);letter-spacing:.04em;text-transform:uppercase}

/* header */
.site-header{position:absolute;top:0;left:0;width:1200px;height:120px;background:var(--forest);}
.brand{position:absolute;left:150px;top:16px;display:flex;align-items:center;gap:12px}
.brand-mark{width:88px;height:88px;border-radius:50%;border:2px solid var(--gold);display:flex;align-items:center;justify-content:center;font:700 26px var(--serif);color:var(--gold)}
.header-actions{position:absolute;right:150px;top:18px;display:flex;gap:14px}
.phone-pill{display:flex;align-items:center;gap:8px;border:1px solid var(--teal-bright);color:var(--white);font:700 13px var(--sans);padding:10px 18px;border-radius:3px}
.main-nav{position:absolute;right:150px;top:80px;display:flex;gap:26px}
.main-nav a{color:var(--white);font:700 12px var(--sans);letter-spacing:.06em;text-decoration:none;text-transform:uppercase;padding-bottom:6px}
.main-nav a.active{color:var(--gold-light);border-bottom:2px solid var(--gold-light)}

/* hero */
.hero{position:absolute;top:120px;left:0;width:1200px;height:640px;background:linear-gradient(180deg,#8fb3cf 0%,#c7d6dc 38%,#a88b6a 62%,#6f5a44 100%)}
.hero-copy{position:absolute;left:600px;top:56px;width:440px;color:var(--white)}
.hero-copy h1{font:700 46px/1.05 var(--serif);text-transform:uppercase;text-shadow:0 2px 8px rgba(0,0,0,.35)}
.hero-copy p{font:700 17px/1.35 var(--serif);margin:16px 0 22px;text-shadow:0 1px 6px rgba(0,0,0,.4)}

/* services */
.services{position:absolute;top:760px;left:0;width:1200px;height:660px;background:var(--mint-pale)}
.services .section-title{position:absolute;top:78px;width:100%;text-align:center;font-size:34px}
.service-cards{position:absolute;left:152px;top:200px;display:flex;gap:15px}
.service-card{width:215px;height:380px;background:var(--white);border-radius:8px;box-shadow:0 4px 14px rgba(12,58,43,.14);overflow:hidden}
.service-card .photo{height:160px}
.service-card h3{font:700 16px var(--sans);color:var(--forest);margin:16px 14px 8px}
.service-card p{font:400 12.5px/1.5 var(--sans);color:var(--muted);margin:0 14px 14px}
.service-card .btn{margin-left:14px;font-size:10px;padding:8px 12px}
.slider-arrow{position:absolute;top:388px;width:40px;height:40px;border-radius:50%;background:var(--forest)}
.slider-arrow svg{display:block;margin:10px}

/* welcome */
.welcome{position:absolute;top:1420px;left:0;width:1200px;height:540px;background:var(--teal)}
.welcome-photo{position:absolute;left:152px;top:62px;width:470px;height:430px;background:linear-gradient(160deg,#8a7a66,#4f5a55 60%,#2f3a36)}
.welcome-copy{position:absolute;left:700px;top:80px;width:380px;color:var(--white)}
.eyebrow{display:inline-block;background:var(--white);color:var(--forest);font:700 11px var(--sans);letter-spacing:.1em;padding:6px 12px;border-radius:2px}
.welcome-copy h2{font:600 30px/1.15 var(--serif);text-transform:uppercase;margin:14px 0 22px}
.welcome-copy p{font:400 13px/1.6 var(--sans);opacity:.92;margin-bottom:72px}

/* approach */
.approach{position:absolute;top:1960px;left:0;width:1200px;height:620px;background:var(--white)}
.approach .section-title{position:absolute;left:152px;top:88px;font-size:34px}
.approach-list{position:absolute;left:152px;top:212px;width:420px;list-style:none}
.approach-list li{display:flex;gap:16px;margin-bottom:34px}
.approach-icon{flex:0 0 44px;height:44px;border-radius:6px;background:var(--teal);display:flex;align-items:center;justify-content:center}
.approach-list h3{font:700 15px var(--sans);color:var(--forest);margin:2px 0 5px}
.approach-list p{font:400 12.5px/1.45 var(--sans);color:var(--muted)}
.approach-feature{position:absolute;left:600px;top:80px;width:480px;height:480px;border-radius:50%;border:10px solid var(--gold);box-shadow:0 0 0 4px var(--forest),0 0 0 10px var(--gold-light)}
.approach-feature div{width:100%;height:100%;border-radius:50%;background:radial-gradient(circle,#e6c98a 0%,#5a4a38 35%,#1f1c18 75%)}

/* community */
.community{position:absolute;top:2580px;left:0;width:1200px;height:760px;background:var(--mint-pale)}
.community .section-title{position:absolute;left:220px;top:88px;width:440px;text-align:center;font-size:34px;line-height:1.2}
.community-copy{position:absolute;left:700px;top:84px;width:380px}
.community-copy p{font:400 13px/1.6 var(--muted);color:var(--muted);font-family:var(--sans);margin-bottom:22px}
.community-photo{position:absolute;left:152px;top:320px;width:896px;height:380px;border-radius:10px;background:linear-gradient(90deg,#2b2522,#7a4a22 40%,#d07a2a 55%,#5a3a22 75%,#231e1b)}

/* call to action */
.cta{position:absolute;top:3340px;left:0;width:1200px;height:460px;background:linear-gradient(90deg,var(--teal) 0%,var(--teal) 40%,#4b8f7c 62%,#6f9c86 100%)}
.cta-copy{position:absolute;left:152px;top:88px;width:420px;color:var(--white)}
.cta-copy h2{font:600 44px/1.1 var(--serif);text-transform:uppercase}
.cta-copy p{font:400 15px/1.5 var(--sans);margin:24px 0 26px}

/* footer */
.site-footer{position:absolute;top:3800px;left:0;width:1200px;height:340px;background:var(--forest-deep);color:var(--white)}
.footer-brand{position:absolute;left:152px;top:40px;display:flex;align-items:center;gap:14px}
.footer-brand .brand-mark{width:110px;height:110px;font-size:32px}
.footer-col{position:absolute;top:56px}
.footer-col h4{font:700 13px var(--sans);letter-spacing:.1em;color:var(--gold-light);margin-bottom:16px;text-transform:uppercase}
.contact-line{display:flex;gap:12px;font:400 12px/1.5 var(--sans);margin-bottom:14px}
.contact-line svg{flex:0 0 16px;margin-top:2px}
.footer-menu{list-style:none}
.footer-menu li{font:400 12px/1.55 var(--sans);text-transform:uppercase}
.social-row{display:flex;gap:10px;margin-bottom:26px}
.social-row span{width:30px;height:30px;border-radius:50%;background:var(--white)}
.copyright{position:absolute;top:4140px;left:0;width:1200px;height:52px;background:#061f17;color:#b8c8c2;font:400 12px/52px var(--sans);text-align:center}
</style>
</head>
<body>

<header class="site-header">
  <div class="brand"><div class="brand-mark">TKR</div></div>
  <div class="header-actions">
    <div class="phone-pill">
      <svg width="14" height="14" viewBox="0 0 24 24" fill="#00ab8e"><path d="M6.6 10.8a15.1 15.1 0 006.6 6.6l2.2-2.2a1 1 0 011-.25 11.4 11.4 0 003.6.57 1 1 0 011 1V20a1 1 0 01-1 1A17 17 0 013 4a1 1 0 011-1h3.5a1 1 0 011 1 11.4 11.4 0 00.57 3.6 1 1 0 01-.25 1z"/></svg>
      +1 (555) 204-1880
    </div>
    <a class="btn" href="#contact">Request a Proposal</a>
  </div>
  <nav class="main-nav">
    <a class="active" href="#">Home</a><a href="#">About</a><a href="#">Our Work</a><a href="#">Services</a><a href="#">Methodology</a><a href="#">Join Our Team</a><a href="#">Contact</a>
  </nav>
</header>

<section class="hero" role="img" aria-label="Civil construction site with a crane lowering large pipe sections into an open trench">
  <div class="hero-copy">
    <h1>Commercial and Civil Construction</h1>
    <p>General Contracting, Design / Build, Construction Management Services</p>
    <a class="btn" href="#">Request a Proposal</a>
  </div>
</section>

<section class="services">
  <h2 class="section-title">What We Do</h2>
  <div class="slider-arrow" style="left:88px"><svg width="20" height="20" viewBox="0 0 20 20"><path d="M13 4l-6 6 6 6" stroke="#fff" stroke-width="2.5" fill="none"/></svg></div>
  <div class="service-cards">
    <article class="service-card">
      <div class="photo" role="img" aria-label="Contractors shaking hands over project plans" style="background:linear-gradient(135deg,#d8c7a8,#7c8a7e)"></div>
      <h3>Prime Contracting</h3>
      <p>Single point of responsibility for scope, schedule and budget, with clear reporting to owners at every stage.</p>
      <a class="btn" href="#">Read More</a>
    </article>
    <article class="service-card">
      <div class="photo" role="img" aria-label="Workers in hard hats beside an excavator on a civil site" style="background:linear-gradient(135deg,#c9a05a,#6d6a5a)"></div>
      <h3>Civil Construction</h3>
      <p>Earthworks, roads, grading and site servicing delivered safely by experienced crews and modern equipment.</p>
      <a class="btn" href="#">Read More</a>
    </article>
    <article class="service-card">
      <div class="photo" role="img" aria-label="Crew installing buried water and sewer pipe" style="background:linear-gradient(135deg,#6a8aa0,#9c7a4c)"></div>
      <h3>Underground Utilities</h3>
      <p>Municipal water, sanitary sewer and storm systems installed, tested and commissioned to specification.</p>
      <a class="btn" href="#">Read More</a>
    </article>
    <article class="service-card">
      <div class="photo" role="img" aria-label="Technicians working on large pipe valves inside a plant" style="background:linear-gradient(135deg,#8a8f94,#4e5a60)"></div>
      <h3>Design-Build Support</h3>
      <p>Early involvement with engineers and consultants to refine design, costing and constructability.</p>
      <a class="btn" href="#">Read More</a>
    </article>
  </div>
  <div class="slider-arrow" style="left:1072px"><svg width="20" height="20" viewBox="0 0 20 20"><path d="M7 4l6 6-6 6" stroke="#fff" stroke-width="2.5" fill="none"/></svg></div>
</section>

<section class="welcome">
  <div class="welcome-photo" role="img" aria-label="Construction workers in safety gear handling pipe on site"></div>
  <div class="welcome-copy">
    <span class="eyebrow">WELCOME TO</span>
    <h2>Tarkwood Ridge Enterprises Ltd</h2>
    <p>We are a prime contractor delivering civil and commercial work for public and private owners. Our team brings decades of field experience, careful planning and a steady focus on safety, quality and long-term value for every community we serve.</p>
    <a class="btn" href="#">Read More</a>
  </div>
</section>

<section class="approach">
  <h2 class="section-title">Our Approach</h2>
  <ul class="approach-list">
    <li><span class="approach-icon"><svg width="22" height="22" viewBox="0 0 24 24" fill="none" stroke="#fff" stroke-width="2"><rect x="4" y="4" width="16" height="16" rx="2"/><path d="M8 9h8M8 13h8M8 17h5"/></svg></span><div><h3>Pre-Construction Planning</h3><p>Risk mitigation, cost certainty, stakeholder alignment</p></div></li>
    <li><span class="approach-icon"><svg width="22" height="22" viewBox="0 0 24 24" fill="none" stroke="#fff" stroke-width="2"><circle cx="8" cy="9" r="3"/><circle cx="16" cy="9" r="3"/><path d="M3 19c1-3 3-4 5-4s4 1 5 4M11 19c1-3 3-4 5-4s4 1 5 4"/></svg></span><div><h3>Collaborative Execution</h3><p>Transparent reporting, strong site leadership, safety-first culture</p></div></li>
    <li><span class="approach-icon"><svg width="22" height="22" viewBox="0 0 24 24" fill="none" stroke="#fff" stroke-width="2.4"><path d="M5 12l5 5 9-10"/></svg></span><div><h3>Quality &amp; Compliance Control</h3><p>Strict adherence to engineering specifications and regulatory standards</p></div></li>
    <li><span class="approach-icon"><svg width="22" height="22" viewBox="0 0 24 24" fill="none" stroke="#fff" stroke-width="2"><path d="M4 20V10M10 20V6M16 20v-8M22 20H2"/></svg></span><div><h3>Long-Term Performance Focus</h3><p>Infrastructure designed and built for durability and sustainability</p></div></li>
  </ul>
  <div class="approach-feature"><div role="img" aria-label="Worker standing inside a large culvert pipe looking toward the light"></div></div>
</section>

<section class="community">
  <h2 class="section-title">Supporting First Nation &amp; Community Infrastructure</h2>
  <div class="community-copy">
    <p>TKR is proud to contribute to the development of essential infrastructure in First Nation communities, ensuring sustainable water, sewer, and public works systems that serve generations to come.</p>
    <a class="btn" href="#">Read More</a>
  </div>
  <div class="community-photo" role="img" aria-label="Worker in orange safety gear inside a large underground pipe"></div>
</section>

<section class="cta">
  <div class="cta-copy">
    <h2>Let's Build Infrastructure That Lasts</h2>
    <p>Whether municipal, industrial, or community-based — TKR delivers structured, reliable, and accountable project execution.</p>
    <a class="btn" href="#">Contact Us</a>
  </div>
</section>

<footer class="site-footer" id="contact">
  <div class="footer-brand"><div class="brand-mark">TKR</div></div>
  <div class="footer-col" style="left:412px;width:240px">
    <h4>Contact Us</h4>
    <div class="contact-line"><svg width="16" height="16" viewBox="0 0 24 24" fill="#d8b15a"><path d="M12 2a7 7 0 00-7 7c0 5 7 13 7 13s7-8 7-13a7 7 0 00-7-7zm0 9.5A2.5 2.5 0 1112 6.5a2.5 2.5 0 010 5z"/></svg><span>4418 RIDGEWAY ROAD, UNIT 12<br>KELMORE, ONTARIO</span></div>
    <div class="contact-line"><svg width="16" height="16" viewBox="0 0 24 24" fill="#d8b15a"><path d="M6.6 10.8a15.1 15.1 0 006.6 6.6l2.2-2.2a1 1 0 011-.25 11.4 11.4 0 003.6.57 1 1 0 011 1V20a1 1 0 01-1 1A17 17 0 013 4a1 1 0 011-1h3.5a1 1 0 011 1 11.4 11.4 0 00.57 3.6 1 1 0 01-.25 1z"/></svg><span>+1 (555) 204-1880</span></div>
    <div class="contact-line"><svg width="16" height="16" viewBox="0 0 24 24" fill="none" stroke="#d8b15a" stroke-width="2"><rect x="3" y="5" width="18" height="14" rx="1"/><path d="M3 6l9 7 9-7"/></svg><span>info@tkrprime.com</span></div>
  </div>
  <div class="footer-col" style="left:700px">
    <h4>Menu</h4>
    <ul class="footer-menu"><li>Home</li><li>About</li><li>Our Work</li><li>Services</li><li>Methodology</li><li>Join Our Team</li><li>Contact</li></ul>
  </div>
  <div class="footer-col" style="left:872px">
    <h4>Follow Us</h4>
    <div class="social-row"><span></span><span></span><span></span><span></span><span></span></div>
    <a class="btn" href="#">Download Profile</a>
  </div>
</footer>
<div class="copyright">Copyright © TKR All Rights Reserved</div>

</body>
</html>
```